Automotive Accessories Business Card

Design a business template that match our new logo design and our industry.

https://www.kelvorauto.com/

Target Market(s)

Aftermarket auto parts and accessories

Industry/Entity Type

automotive

Contact Information for Business Card

company logo

Font styles to use
Serif
Sans Serif

Colors
EB3D1F
EC4F4E
F09395
F8D3D4
FCEDEE

```html
<!DOCTYPE html>
<html lang="en">
<head>
<meta charset="utf-8">
<title>Kelvor Auto – Business Card</title>
<link href="https://fonts.googleapis.com/css2?family=Montserrat:wght@400;500;700;800&display=swap" rel="stylesheet">
<style>
  :root {
    --bg: #1d1d1e;
    --card-dark: #3d3c3e;
    --card-light: #ffffff;
    --brand-red: #d81f26;
    --text-light: #ffffff;
    --shadow: rgba(0,0,0,0.55);
  }
  * { margin: 0; padding: 0; box-sizing: border-box; }
  html, body {
    width: 1200px; height: 988px; overflow: hidden;
    background: var(--bg);
    font-family: "Montserrat", sans-serif;
  }
  .canvas { position: relative; width: 1200px; height: 988px; }
  .card {
    position: absolute;
    width: 520px; height: 297px;
    border-radius: 18px;
    overflow: hidden;
    box-shadow: 0 14px 30px var(--shadow);
  }
  .card-back { left: 80px; top: 130px; background: var(--card-dark); }
  .card-front { left: 600px; top: 560px; background: var(--card-light); }
  .card-shape { position: absolute; inset: 0; width: 100%; height: 100%; }

  .brand {
    position: absolute;
    display: flex; align-items: center; gap: 10px;
    font-weight: 800;
    color: var(--brand-red);
    letter-spacing: 1px;
    text-transform: uppercase;
    white-space: nowrap;
  }
  .brand-square { width: 16px; height: 16px; background: var(--brand-red); flex: none; }
  .card-back .brand { left: 50%; top: 50%; transform: translate(-50%, -50%); font-size: 36px; }
  .card-back .brand-square { width: 24px; height: 24px; }
  .card-front .brand { right: 40px; top: 28px; font-size: 26px; }

  .contact {
    position: absolute; left: 40px; top: 140px;
    color: var(--text-light);
    white-space: nowrap;
  }
  .contact-name {
    font-weight: 800; font-size: 19px; letter-spacing: 1px; line-height: 23px;
    color: var(--brand-red); text-transform: uppercase;
  }
  .contact-title { font-size: 12px; line-height: 16px; margin-top: 1px; }
  .divider { width: 14px; height: 2px; background: var(--brand-red); margin: 7px 0 5px; }
  .contact-line {
    display: flex; align-items: center; gap: 8px;
    font-size: 12px; line-height: 18px;
  }
  .contact-line svg { width: 11px; height: 11px; fill: var(--brand-red); flex: none; }
  .contact-address { font-size: 12px; line-height: 16px; }
</style>
</head>
<body>
<main class="canvas">

  <section class="card card-back" aria-label="Card back">
    <div class="brand"><span class="brand-square"></span>Kelvor Auto</div>
  </section>

  <section class="card card-front" aria-label="Card front">
    <svg class="card-shape" viewBox="0 0 520 297" preserveAspectRatio="none">
      <path fill="var(--card-dark)" d="M0,297 L0,150 C20,120 90,108 250,104 C390,100 480,96 520,62 L520,297 Z"/>
      <path fill="none" stroke="var(--brand-red)" stroke-width="5" d="M150,108 C200,104 220,103 250,102 C390,98 478,94 522,56"/>
    </svg>

    <div class="brand"><span class="brand-square"></span>Kelvor Auto</div>

    <div class="contact">
      <div class="contact-name">Dana Whitlow</div>
      <div class="contact-title">CEO/Founder</div>
      <div class="divider"></div>
      <div class="contact-line">
        <svg viewBox="0 0 24 24"><path d="M6.6 10.8a15.1 15.1 0 0 0 6.6 6.6l2.2-2.2a1 1 0 0 1 1-.25 11.4 11.4 0 0 0 3.6.57 1 1 0 0 1 1 1V20a1 1 0 0 1-1 1A17 17 0 0 1 3 4a1 1 0 0 1 1-1h3.5a1 1 0 0 1 1 1c0 1.25.2 2.45.57 3.57a1 1 0 0 1-.25 1z"/></svg>
        1-800-555-0142
      </div>
      <div class="contact-line">
        <svg viewBox="0 0 24 24"><path d="M2 5h20v14H2z M2 5l10 8 10-8"/></svg>
        sales@kelvorauto.com
      </div>
      <div class="contact-line">
        <svg viewBox="0 0 24 24"><circle cx="12" cy="12" r="10"/></svg>
        www.kelvorauto.com
      </div>
      <div class="divider"></div>
      <div class="contact-address">240 W. Harbor Ave. Unit B Fairview, CA, 90412</div>
    </div>
  </section>

</main>
</body>
</html>
```